Business Cards and email stationery for VoiceOver Artist
Cutting Edge Business cards and email stationery for VoiceOver Artist
Use standard fonts
Not sure here?
Bright & Fun-filled
Marcus Dellow
Voiceover
2817 Palmera Ave
Encino CA 91427
(•••NO ADDRESS ON BUSINESS CARDS PLEASE••••)
818-555-2193 Cell
marcus@marcusdellow.example
marcusdellow.example
As 3-D as possible, cutting-edge, creative
1 Should be easy to read
2 Cell number should be listed first!
Uploaded Logo for VoiceOver Artist for Business cards and email Stationery
Logo for VoiceOver Artist v2

```html
<!DOCTYPE html>
<html lang="en">
<head>
<meta charset="utf-8">
<title>Marcus Dellow — Voiceover Business Card</title>
<link rel="stylesheet" href="https://fonts.googleapis.com/css2?family=Michroma&family=Montserrat:wght@400;500;600&display=swap">
<style>
  :root {
    --page-bg: #e9e7e4;
    --red-light: #e42a26;
    --red-mid: #c3130f;
    --red-dark: #7d0705;
    --graphite: #4b4b4d;
    --graphite-dark: #3a3a3c;
    --silver: #d9d9db;
    --silver-dark: #9c9ca0;
    --text-light: #f1f1f1;
    --text-muted: #c9c9cb;
    --card-shadow: rgba(0, 0, 0, 0.28);
  }
  * { box-sizing: border-box; margin: 0; padding: 0; }
  html, body {
    width: 1200px; height: 629px; overflow: hidden;
    background: var(--page-bg);
  }
  .canvas {
    width: 1200px; height: 629px;
    display: flex; align-items: center; justify-content: center; gap: 60px;
  }
  .card {
    position: relative;
    width: 520px; height: 297px;
    border-radius: 4px; overflow: hidden;
    box-shadow: 0 10px 28px var(--card-shadow);
    font-family: "Montserrat", sans-serif;
  }
  .red-surface {
    background: radial-gradient(ellipse at 55% 35%, var(--red-light) 0%, var(--red-mid) 45%, var(--red-dark) 100%);
  }

  /* Front side */
  .card-front .emblem {
    position: absolute; left: 50%; top: 42%;
    transform: translate(-50%, -50%);
    display: flex; flex-direction: column; align-items: center; gap: 14px;
  }
  .emblem-disc {
    width: 74px; height: 74px; border-radius: 50%;
    background: radial-gradient(circle at 35% 30%, #ffffff 0%, var(--silver) 40%, var(--silver-dark) 100%);
    box-shadow: 0 3px 8px rgba(0,0,0,0.35);
  }
  .emblem-name {
    font-family: "Michroma", sans-serif;
    font-size: 15px; letter-spacing: 3px;
    color: var(--silver);
  }
  .front-web {
    position: absolute; left: 28px; bottom: 24px;
    font-size: 9px; letter-spacing: 3.5px;
    color: var(--text-muted); text-transform: uppercase;
  }

  /* Back side */
  .card-back { display: flex; flex-direction: column; }
  .back-top {
    height: 56%; position: relative;
    border-bottom: 2px solid var(--silver);
  }
  .back-bottom {
    flex: 1;
    background: linear-gradient(180deg, var(--graphite) 0%, var(--graphite-dark) 100%);
    display: flex; align-items: center; justify-content: center; gap: 16px;
  }
  .brand-lockup {
    position: absolute; left: 30px; bottom: 22px;
    display: flex; align-items: center; gap: 12px;
  }
  .brand-disc {
    width: 36px; height: 36px; border-radius: 50%;
    background: radial-gradient(circle at 35% 30%, #ffffff 0%, var(--silver) 40%, var(--silver-dark) 100%);
    box-shadow: 0 2px 5px rgba(0,0,0,0.35);
  }
  .brand-text { display: flex; flex-direction: column; gap: 4px; }
  .brand-name {
    font-family: "Michroma", sans-serif;
    font-size: 20px; letter-spacing: 1px;
    color: var(--silver);
  }
  .brand-tagline {
    font-size: 8px; letter-spacing: 9px;
    color: var(--text-muted); text-transform: uppercase;
  }
  .identity { text-align: right; }
  .identity-name {
    font-size: 12px; letter-spacing: 3px; font-weight: 500;
    color: var(--text-light); text-transform: uppercase;
  }
  .identity-role {
    margin-top: 4px;
    font-size: 9px; letter-spacing: 3px;
    color: var(--text-muted); text-transform: uppercase;
  }
  .divider { width: 1px; height: 56px; background: var(--text-muted); }
  .contact-list { list-style: none; display: flex; flex-direction: column; gap: 7px; }
  .contact-item {
    display: flex; align-items: center; gap: 7px;
    font-size: 9.5px; letter-spacing: 0.6px; color: var(--text-light);
  }
  .contact-icon {
    width: 12px; height: 12px; flex: none;
  }
</style>
</head>
<body>
<main class="canvas">

  <section class="card card-front red-surface" aria-label="Business card front">
    <div class="emblem">
      <div class="emblem-disc"></div>
      <div class="emblem-name">MARCUS DELLOW</div>
    </div>
    <p class="front-web">www.marcusdellow.example</p>
  </section>

  <section class="card card-back" aria-label="Business card back">
    <div class="back-top red-surface">
      <div class="brand-lockup">
        <div class="brand-disc"></div>
        <div class="brand-text">
          <span class="brand-name">MARCUSDELLOW</span>
          <span class="brand-tagline">Voiceover</span>
        </div>
      </div>
    </div>
    <div class="back-bottom">
      <div class="identity">
        <p class="identity-name">Marcus Dellow</p>
        <p class="identity-role">Voiceover</p>
      </div>
      <div class="divider"></div>
      <ul class="contact-list">
        <li class="contact-item">
          <svg class="contact-icon" viewBox="0 0 12 12"><circle cx="6" cy="6" r="6" fill="#d9d9db"/><rect x="4" y="2.5" width="4" height="7" rx="0.8" fill="#4b4b4d"/></svg>
          818-555-2193 Cell
        </li>
        <li class="contact-item">
          <svg class="contact-icon" viewBox="0 0 12 12"><circle cx="6" cy="6" r="6" fill="#d9d9db"/><rect x="3" y="4" width="6" height="4.2" fill="none" stroke="#4b4b4d" stroke-width="0.9"/><path d="M3 4 L6 6.4 L9 4" fill="none" stroke="#4b4b4d" stroke-width="0.9"/></svg>
          marcus@marcusdellow.example
        </li>
        <li class="contact-item">
          <svg class="contact-icon" viewBox="0 0 12 12"><circle cx="6" cy="6" r="6" fill="#d9d9db"/><circle cx="6" cy="6" r="3" fill="none" stroke="#4b4b4d" stroke-width="0.9"/><path d="M3 6 H9 M6 3 V9" stroke="#4b4b4d" stroke-width="0.7"/></svg>
          www.marcusdellow.example
        </li>
      </ul>
    </div>
  </section>

</main>
</body>
</html>
```